Timid Kitten Clinic Business Card Design

I need a business card designed for my cat only veterinary clinic. I will upload the logo that I would like included on the card. Please include:
Business Name: The Timid Kitten Clinic
Address: 4827 W. 39th Ln, Scottsdale, AZ 85317
Phone #: 480-555-6314
Website URL: www.timidkittenvet.example
And the Doctors Name: Marla Quint, DVM

```html
<!DOCTYPE html>
<html lang="en">
<head>
<meta charset="utf-8">
<title>Timid Kitten Clinic – Business Card</title>
<link rel="stylesheet" href="https://fonts.googleapis.com/css2?family=Comfortaa:wght@400;700&family=Fira+Sans:wght@400&family=Montserrat:wght@500;700&display=swap">
<style>
  :root {
    --stage: #252525;
    --card: #ffffff;
    --ink: #1a1a1a;
    --service: #4a4a4a;
    --dot: #8e9fd6;
    --teal: #0f4c68;
    --sky: #5b86c4;
    --wall: #eef0f2;
    --logo-ring: #2c2236;
  }
  * { box-sizing: border-box; margin: 0; padding: 0; }
  html, body { width: 1200px; height: 1200px; overflow: hidden; background: var(--stage); }
  .stage { position: relative; width: 1200px; height: 1200px; }

  .card {
    position: absolute;
    left: 240px;
    width: 720px;
    height: 410px;
    border-radius: 26px;
    overflow: hidden;
    background: var(--card);
  }
  .card--front { top: 150px; }
  .card--back { top: 630px; background: var(--wall); }

  /* Front */
  .front-photo {
    position: absolute; right: 0; top: 0; width: 330px; height: 100%;
    background:
      linear-gradient(90deg, #ffffff 0%, rgba(255,255,255,0) 35%),
      radial-gradient(ellipse at 65% 45%, #3b2e33 0%, #8a6a6e 30%, #e6d4cf 60%, #f7efe9 100%);
  }
  .brand { position: absolute; left: 58px; top: 46px; display: flex; align-items: center; gap: 14px; }
  .brand-mark { width: 134px; height: 134px; border-radius: 50%; background: var(--logo-ring); }
  .brand-name {
    font-family: "Comfortaa", sans-serif; font-weight: 700; font-size: 30px;
    line-height: 1.08; letter-spacing: 2px; color: var(--ink);
  }
  .services {
    position: absolute; left: 40px; top: 212px; width: 470px;
    font-family: "Fira Sans", sans-serif; font-size: 16px; color: var(--service);
    line-height: 2.35; text-align: center;
  }
  .services .sep { color: var(--dot); margin: 0 8px; }

  /* Back */
  .back-photo {
    position: absolute; inset: 0;
    background:
      linear-gradient(180deg, rgba(238,240,242,0) 30%, rgba(238,240,242,0) 62%, var(--wall) 80%),
      linear-gradient(170deg, var(--wall) 0%, var(--wall) 32%, #8c7f6c 40%, #6f6354 52%, #a49883 62%, var(--wall) 72%);
  }
  .doctor { position: absolute; right: 50px; top: 118px; text-align: left; }
  .doctor-name {
    font-family: "Montserrat", sans-serif; font-weight: 700; font-size: 34px; color: var(--teal);
  }
  .doctor-role {
    font-family: "Montserrat", sans-serif; font-weight: 500; font-size: 24px; color: var(--sky);
    margin-left: 56px; margin-top: -6px;
  }
  .contact {
    position: absolute; left: 52px; bottom: 56px; list-style: none;
    font-family: "Montserrat", sans-serif; font-weight: 700; font-size: 18px; color: var(--teal);
  }
  .contact li { display: flex; align-items: center; gap: 10px; line-height: 1.45; }
  .contact svg { width: 17px; height: 17px; fill: var(--sky); flex: none; }
  .social {
    position: absolute; right: 36px; bottom: 100px; display: flex; align-items: center; gap: 8px;
    font-family: "Montserrat", sans-serif; font-weight: 500; font-size: 16px; color: var(--teal);
    white-space: nowrap;
  }
  .social-dot { width: 11px; height: 11px; border-radius: 50%; background: var(--teal); }
  .social-name { font-weight: 700; }
</style>
</head>
<body>
<main class="stage">

  <section class="card card--front">
    <div class="front-photo" role="img" aria-label="Photo of a long-haired seal-point cat resting by a sunny window"></div>
    <div class="brand">
      <div class="brand-mark"></div>
      <h1 class="brand-name">The Timid Kitten<br>Clinic</h1>
    </div>
    <p class="services">
      Feline Dentistry<span class="sep">•</span>Surgery<span class="sep">•</span>Diagnostics<span class="sep">•</span>Cold Laser Therapy<br>
      Cat Boarding Services<span class="sep">•</span>Cat Grooming Services<br>
      Feline Behavioral Therapy<span class="sep">•</span>Telemedicine Services
    </p>
  </section>

  <section class="card card--back">
    <div class="back-photo" role="img" aria-label="Photo of a tabby cat lounging stretched out on a white wall ledge"></div>
    <div class="doctor">
      <h2 class="doctor-name">Marla Quint, DVM</h2>
      <p class="doctor-role">Director / Doctor</p>
    </div>
    <ul class="contact">
      <li>
        <svg viewBox="0 0 24 24"><path d="M6.6 10.8a15.1 15.1 0 0 0 6.6 6.6l2.2-2.2a1 1 0 0 1 1-.25 11.4 11.4 0 0 0 3.6.57 1 1 0 0 1 1 1V20a1 1 0 0 1-1 1A17 17 0 0 1 3 4a1 1 0 0 1 1-1h3.5a1 1 0 0 1 1 1c0 1.250.2 2.450.57 3.570a1 1 0 0 1-.25 1z"/></svg>
        (480) 555-6314
      </li>
      <li>
        <svg viewBox="0 0 24 24"><path d="M12 2a10 10 0 1 0 0 20 10 10 0 0 0 0-20zm6.9 6h-2.9a15.7 15.7 0 0 0-1.4-3.6A8 8 0 0 1 18.9 8zM12 4c.8 1.2 1.5 2.5 1.9 4h-3.8c.4-1.5 1.1-2.8 1.9-4zM4.3 14a8 8 0 0 1 0-4h3.4a16 16 0 0 0 0 4zm.8 2h2.9c.3 1.3.8 2.5 1.4 3.6A8 8 0 0 1 5.1 16zM8 8H5.1a8 8 0 0 1 4.3-3.6C8.8 5.5 8.4 6.7 8 8zm4 12c-.8-1.2-1.5-2.5-1.9-4h3.8c-.4 1.5-1.1 2.8-1.9 4zm2.3-6H9.7a14.7 14.7 0 0 1 0-4h4.6a14.7 14.7 0 0 1 0 4zm.3 5.6c.6-1.1 1.1-2.3 1.4-3.6h2.9a8 8 0 0 1-4.3 3.6zm1.7-5.6a16 16 0 0 0 0-4h3.4a8 8 0 0 1 0 4z"/></svg>
        www.timidkittenvet.example
      </li>
      <li>
        <svg viewBox="0 0 24 24"><path d="M12 2a7 7 0 0 0-7 7c0 5.2 7 13 7 13s7-7.8 7-13a7 7 0 0 0-7-7zm0 9.5A2.5 2.5 0 1 1 12 6.5a2.5 2.5 0 0 1 0 5z"/></svg>
        4827 W. 39th Ln, Scottsdale, AZ 85317
      </li>
    </ul>
    <div class="social">
      <span>Find us on:</span>
      <span class="social-dot"></span><span class="social-name">Pawbook</span>
      <span class="social-name">Snapfeed</span>
    </div>
  </section>

</main>
</body>
</html>
```